Wrenmoor Hall Business Cards design with a logo

I want two Business cards designed with a very modern contemporary logo UNING 1920'S FONT STYLES with the following details

Address:
Wrenmoor Hall
17 Pellamy Road
Kelvinbrae
G62 3LT

Details for card 1

Name: Dorian Ashby
email: Dorian.ashby@wrenmoor.example
Tel : +971 50 318 2964
Tel +44 7700 900 418

Details Card 2

Name: Dorian Ashby
email: Trevor.lindqvist@wrenmoor.example
Tel : +971 50 274 6153

Wrenmoor hall is a house that was built around 1880 and was used extensively in the 1920's for entertaining and parties in the arts scene, the house again will be resurrected to a modern entertainment venue

If you have any questions feel free to ask

Target Market(s)

The market for this is the young modern crowd

Industry/Entity Type

Entertainment Industry

Contact Information for Business Card

Address:
Wrenmoor Hall
17 Pellamy Road
Kelvinbrae
G62 3LT

Details for card 1

Name: Dorian Ashby
Tel : +971 50 318 2964
Tel +44 7700 900 418

Details Card 2

Name: Trevor Lindqvist
Tel : +971 50 274 6153

Logo Text

Wrenmoor Hall

Font styles to use
Other font styles liked:
• 1920'S FONT STULES

Requirements
Must have
• Modern Contemporary, whilst taking into consideration the age of the house as detailed above. YOU MUT BE USING 1920'S FONT STYLES
Nice to have
• 1920'S FONT STYLES see attached image if a suggestion
Should not have
• Should not look old or dated

```html
<!DOCTYPE html>
<html lang="en">
<head>
<meta charset="utf-8">
<title>Wrenmoor Hall — Business Cards</title>
<link href="https://fonts.googleapis.com/css2?family=Oswald:wght@600&family=Work+Sans:wght@400;500;600&display=swap" rel="stylesheet">
<style>
  :root {
    --backdrop: #2a2a2b;
    --card: #1d1d1e;
    --card-edge: #232324;
    --accent: #f4e21a;
    --ink: #f2f2f2;
  }
  * { box-sizing: border-box; margin: 0; padding: 0; }
  html, body { width: 1200px; height: 900px; overflow: hidden; }
  body {
    background: var(--backdrop);
    font-family: "Work Sans", Arial, sans-serif;
    color: var(--ink);
    position: relative;
  }
  .card {
    position: absolute;
    left: 290px;
    width: 620px;
    height: 354px;
    background: linear-gradient(160deg, var(--card-edge), var(--card));
    border-bottom: 4px solid var(--accent);
  }
  .card--front { top: 70px; }
  .card--back { top: 474px; }

  .brand {
    position: absolute;
    top: 128px; left: 0; right: 0;
    display: flex; align-items: center; justify-content: center; gap: 16px;
  }
  .brand__mark { width: 30px; height: 30px; background: var(--accent); }
  .brand__name {
    font-weight: 500;
    font-size: 52px;
    letter-spacing: 1px;
    color: var(--ink);
    white-space: nowrap;
  }
  .site { font-size: 15px; letter-spacing: 0.5px; }
  .site__domain { color: var(--accent); }
  .card--front .site {
    position: absolute; bottom: 26px; left: 0; right: 0; text-align: center;
  }

  .person {
    position: absolute; top: 128px; right: 338px; text-align: right;
  }
  .person__name {
    font-family: "Oswald", "Arial Narrow", sans-serif;
    font-weight: 600;
    font-size: 34px;
    color: var(--accent);
    letter-spacing: 0.5px;
    line-height: 1.1;
    white-space: nowrap;
  }
  .person__role { font-size: 15px; letter-spacing: 1px; margin-top: 2px; }
  .divider {
    position: absolute; top: 130px; left: 300px;
    width: 2px; height: 72px; background: var(--accent);
  }
  .contacts {
    position: absolute; top: 138px; left: 322px;
    list-style: none; font-size: 14px; letter-spacing: 0.6px; line-height: 20px;
    white-space: nowrap;
  }
  .contacts li { display: flex; align-items: center; gap: 10px; }
  .contacts svg { width: 11px; height: 11px; flex: none; }
  .address {
    position: absolute; bottom: 30px; left: 36px;
    display: flex; align-items: center; gap: 12px;
    font-size: 16px; letter-spacing: 0.8px;
    white-space: nowrap;
  }
  .address__mark { width: 18px; height: 18px; background: var(--accent); }
  .address__venue { color: var(--accent); }
</style>
</head>
<body>
  <section class="card card--front">
    <div class="brand">
      <span class="brand__mark"></span>
      <span class="brand__name">Wrenmoor Hall</span>
    </div>
    <p class="site">www.<span class="site__domain">wrenmoorhall</span>.example</p>
  </section>

  <section class="card card--back">
    <div class="person">
      <h1 class="person__name">DORIAN ASHBY</h1>
      <p class="person__role">Director</p>
    </div>
    <div class="divider"></div>
    <ul class="contacts">
      <li><svg viewBox="0 0 12 12"><path d="M3 1l2 2-1 1.5c.7 1.5 2 2.8 3.5 3.5L9 7l2 2-1.5 2C5 10.5 1.5 7 1 2.5z" fill="var(--accent)"/></svg>+971 50 318 2964</li>
      <li><svg viewBox="0 0 12 12"><path d="M1 4c2-2 8-2 10 0l-1 2-2-1V4H4v1L2 6z M3 7h6l1 4H2z" fill="var(--accent)"/></svg>+44 7700 900 418</li>
      <li><svg viewBox="0 0 12 12"><rect x="1" y="2.5" width="10" height="7" fill="none" stroke="var(--accent)" stroke-width="1.2"/><path d="M1 3l5 4 5-4" fill="none" stroke="var(--accent)" stroke-width="1.2"/></svg>Dorian.ashby@wrenmoor.example</li>
      <li><svg viewBox="0 0 12 12"><g fill="none" stroke="var(--accent)" stroke-width="1"><circle cx="6" cy="6" r="5"/><ellipse cx="6" cy="6" rx="2.2" ry="5"/><path d="M1 6h10"/></g></svg><span class="site">www.<span class="site__domain">wrenmoorhall</span>.example</span></li>
    </ul>
    <p class="address">
      <span class="address__mark"></span>
      <span><span class="address__venue">Wrenmoor Hall,</span> 17 Pellamy Road Kelvinbrae&nbsp;&nbsp;G62 3LT</span>
    </p>
  </section>
</body>
</html>
```